Skin care manufacturer looking for packaging design for new skin care brand.

We need a design and logo for a skin care brand to be sold at retail stores and online in the United States and Europe. The design will be for 1.7oz - 2oz serums that will not have a retail box. The name of the brand is Velvet Meadow and should be a luxurious brand that is approachable. The brand will consist of 4 face serums - Vitamin C, Collagen, Retinol and Hyaluronic Acid. Images shown are for inspiration only. Color of bottles can be varied based on design and bottles can be screen printed or labeled.
Updates

Need extra days to review

Target Market(s)

Target market is 30+ female

Industry/Entity Type

Beauty

Requirements
Must have
• Ingredient call outs + benefit. Ex: Vitamin C Brightening Serum. Packaging should be translucent

```html
<!DOCTYPE html>
<html lang="en">
<head>
<meta charset="utf-8">
<title>Velvet Meadow – Vitamin C Brightening Serum</title>
<link href="https://fonts.googleapis.com/css2?family=Montserrat:wght@300;400;500&display=swap" rel="stylesheet">
<style>
  :root {
    --bg-centre: #3d3536;
    --bg-edge: #241f20;
    --bottle-dark: #1c1819;
    --bottle-mid: #4a4344;
    --gold-light: #f3e3b0;
    --gold-mid: #c9a556;
    --gold-dark: #7a5a22;
    --ink-white: #ffffff;
    --accent-yellow: #e4e135;
  }
  html, body {
    margin: 0;
    padding: 0;
    width: 1200px;
    height: 1200px;
    overflow: hidden;
  }
  body {
    background: radial-gradient(ellipse at 50% 55%, var(--bg-centre) 0%, var(--bg-edge) 80%);
    font-family: "Montserrat", sans-serif;
  }
  .canvas {
    position: relative;
    width: 1200px;
    height: 1200px;
  }
  .bottle-cap {
    position: absolute;
    left: 532px;
    top: 76px;
    width: 130px;
    height: 256px;
    border-radius: 10px 10px 4px 4px;
    background: linear-gradient(90deg, var(--gold-dark) 0%, var(--gold-mid) 22%, var(--gold-light) 48%, var(--gold-mid) 72%, var(--gold-dark) 100%);
  }
  .bottle-body {
    position: absolute;
    left: 486px;
    top: 334px;
    width: 220px;
    height: 606px;
    border-radius: 22px 22px 10px 10px;
    background: linear-gradient(90deg, var(--bottle-dark) 0%, var(--bottle-mid) 42%, var(--bottle-mid) 55%, var(--bottle-dark) 100%);
  }
  .brand-name,
  .product-name {
    position: absolute;
    white-space: nowrap;
    color: var(--ink-white);
    transform: translate(-50%, -50%) rotate(-90deg);
  }
  .brand-name {
    left: 604px;
    top: 652px;
    font-size: 31px;
    font-weight: 500;
    letter-spacing: 9px;
    text-transform: uppercase;
  }
  .product-name {
    left: 640px;
    top: 660px;
    font-size: 15px;
    font-weight: 300;
    letter-spacing: 11.5px;
    text-transform: uppercase;
  }
  .ingredient-arc {
    position: absolute;
    left: 544px;
    top: 392px;
    width: 120px;
    height: 50px;
    overflow: visible;
  }
  .ingredient-arc text {
    fill: var(--accent-yellow);
    font-family: "Montserrat", sans-serif;
    font-size: 15px;
    font-weight: 300;
    letter-spacing: 0.5px;
  }
  .volume {
    position: absolute;
    left: 616px;
    top: 893px;
    color: var(--ink-white);
    font-size: 16px;
    font-weight: 300;
  }
</style>
</head>
<body>
  <main class="canvas">
    <div class="bottle-cap"></div>
    <div class="bottle-body"></div>

    <svg class="ingredient-arc" viewBox="0 0 120 50" aria-label="Vitamin C">
      <defs>
        <path id="ingredient-curve" d="M 6 42 A 62 62 0 0 1 114 42"/>
      </defs>
      <text><textPath href="#ingredient-curve" startOffset="50%" text-anchor="middle">VITAMIN C</textPath></text>
    </svg>

    <div class="brand-name">Velvet Meadow</div>
    <div class="product-name">Brightening Serum</div>
    <div class="volume">1.7oz</div>
  </main>
</body>
</html>
```